Hall of Fame annnouncement graphic for social media

I need a social media Hall of Fame announcement designed in the styles of some of the examples I've posted. I have attached the two gentlemens head shots ... the names are Dale Prusky and Ted Marrish

It is for the BRANDMOOR LINKS HALL OF FAME also include 2026 Inductees ... I have also attached the logo... make the post in similar colors as the logo.

I need this tomorrow so I am going to pick a winner in the next 24 hours.

```html
<!DOCTYPE html>
<html lang="en">
<head>
<meta charset="utf-8">
<title>Brandmoor Links Hall of Fame – 2026 Inductees</title>
<link rel="stylesheet" href="https://fonts.googleapis.com/css2?family=Figtree:ital,wght@0,800;1,400&display=swap">
<style>
  :root {
    --backdrop: #e4e5e7;
    --card: #dddddd;
    --navy: #163054;
    --royal: #0c2d82;
    --white: #ffffff;
    --photo-warm-top: #efe7e1;
    --photo-warm-bottom: #d9c9be;
    --photo-sky-top: #d9dde6;
    --photo-sky-bottom: #a9b79a;
  }
  * { box-sizing: border-box; margin: 0; padding: 0; }
  html, body {
    width: 1200px;
    height: 751px;
    overflow: hidden;
    background: var(--backdrop);
  }
  .stage {
    position: relative;
    width: 1200px;
    height: 751px;
    background: var(--backdrop);
  }
  .announcement {
    position: absolute;
    left: 87px;
    top: 87px;
    width: 1027px;
    height: 578px;
    background: var(--card);
    overflow: hidden;
  }
  .announcement__shapes {
    position: absolute;
    inset: 0;
  }
  .band { fill: var(--navy); }
  .wordmark {
    position: absolute;
    left: 97px;
    top: 222px;
    width: 530px;
    text-align: center;
    font-family: "Figtree", sans-serif;
    font-weight: 800;
    color: var(--royal);
    line-height: 1.05;
    letter-spacing: 1px;
  }
  .wordmark__line { display: block; font-size: 44px; }
  .inductees-year {
    position: absolute;
    left: 199px;
    top: 386px;
    width: 280px;
    text-align: center;
    font-family: "Figtree", sans-serif;
    font-style: italic;
    font-weight: 400;
    font-size: 28px;
    color: var(--royal);
  }
  .nameplate {
    position: absolute;
    height: 57px;
    width: 215px;
    background: var(--navy);
    color: var(--white);
    font-family: "Figtree", sans-serif;
    font-weight: 800;
    font-size: 29px;
    line-height: 57px;
    letter-spacing: -0.3px;
    white-space: nowrap;
  }
  .nameplate--first { left: 693px; top: 231px; padding-left: 26px; }
  .nameplate--second { left: 683px; top: 489px; padding-left: 17px; }
</style>
</head>
<body>
<div class="stage">
  <section class="announcement">
    <svg class="announcement__shapes" width="1027" height="578" viewBox="0 0 1027 578" aria-hidden="false">
      <defs>
        <linearGradient id="portrait-warm" x1="0" y1="0" x2="0" y2="1">
          <stop offset="0" stop-color="var(--photo-warm-top)"/>
          <stop offset="1" stop-color="var(--photo-warm-bottom)"/>
        </linearGradient>
        <linearGradient id="portrait-course" x1="0" y1="0" x2="0" y2="1">
          <stop offset="0" stop-color="var(--photo-sky-top)"/>
          <stop offset="1" stop-color="var(--photo-sky-bottom)"/>
        </linearGradient>
      </defs>
      <polygon class="band band--left" points="0,0 82,0 40,578 0,578"/>
      <polygon class="band band--right" points="988,0 1027,0 1027,578 936,578"/>
      <polygon class="portrait" role="img" aria-label="Headshot of inductee Dale Prusky in a white polo"
               points="740,44 879,44 864,231 722,231" fill="url(#portrait-warm)" stroke="#ffffff" stroke-width="1"/>
      <polygon class="portrait" role="img" aria-label="Headshot of inductee Ted Marrish on a golf course"
               points="729,302 868,302 855,489 712,489" fill="url(#portrait-course)" stroke="#ffffff" stroke-width="1"/>
    </svg>

    <h1 class="wordmark">
      <span class="wordmark__line">BRANDMOOR LINKS</span>
      <span class="wordmark__line">HALL OF FAME</span>
    </h1>
    <p class="inductees-year">2026 Inductees</p>

    <div class="nameplate nameplate--first">Dale Prusky</div>
    <div class="nameplate nameplate--second">Ted Marrish</div>
  </section>
</div>
</body>
</html>
```